Water Filtration Company needs a business card design using our existing logo/colours!

We design and manufacture and export specialised water filtration equipment. Our equipment will take unclean dirty water and filters to safe clean drinkable water.
We would like to see designs using our existing logo and colours (see attached "Palette") that represents clean safe drinking water (fresh, clean designs but still professional and modern). Our customers are other businesses who supply water filtration equipment, governments, and private individuals.
BUSINESS CARD DETAILS (Common details):
Tel: + 61 7 55 419 276
www: brindlepeak.com.au
Address: 3/47 Cordwell Parade
Marlow Flats NSW 2593 Australia
(please include the word Australia as we are an international company)
Must include: COMMERCIAL WATER FILTRATION EQUIPMENT
NAME NO 1:
Owen Pritch
General Manager
Mobile: +61 427 38 91 04
Email: owen@brindlepeak.com.au
NAME NO. 2:
Gina Rosk
Business Manager
Mobile: +61 409 572 148
Email: gina@brindlepeak.com.au
Must Have:
1) PRINT READY IN .AI & .PDF FORMATS
2) Also saved in file format .ai (Adobe Illustrator - compatible with CS4)
3) Use existing LOGO & COLOURS: Please use our logo (see attached file)
4) FONTS: we have used Avenir & Helvetica in the past but are open to other font types for the address etc.
Thank you!

```html
<!DOCTYPE html>
<html lang="en">
<head>
<meta charset="utf-8">
<title>Brindle Peak – Business Card</title>
<link rel="stylesheet" href="https://fonts.googleapis.com/css2?family=Mulish:wght@400;600&display=swap">
<style>
  :root {
    --backdrop: #d6d6d6;
    --card-white: #ffffff;
    --teal-light: #3cbfcb;
    --teal-mid: #1b9db4;
    --teal-deep: #08698a;
    --ink-navy: #0f4f73;
    --ink-teal: #27a2b7;
  }
  * { box-sizing: border-box; margin: 0; padding: 0; }
  html, body {
    width: 1200px; height: 800px; overflow: hidden;
    background: var(--backdrop);
    font-family: "Mulish", "Helvetica Neue", Arial, sans-serif;
  }
  .canvas { position: relative; width: 1200px; height: 800px; }

  .card {
    position: absolute; left: 365px; width: 455px; height: 251px;
    overflow: hidden;
  }
  .card-front {
    top: 127px;
    background: linear-gradient(to bottom,
      var(--teal-mid) 0%, #0f86a2 35%, var(--teal-deep) 50%,
      #1a93ab 75%, var(--teal-light) 100%);
  }
  .brand-name {
    position: absolute; left: 0; right: 0; top: 92px;
    text-align: center;
    color: var(--card-white);
    font-weight: 600; font-size: 54px; letter-spacing: 1px;
    line-height: 1;
  }

  .card-back { top: 400px; background: var(--card-white); }
  .name-band {
    position: absolute; left: 0; right: 0; top: 28px; height: 28px;
    background: linear-gradient(to bottom, var(--teal-mid), var(--teal-deep));
  }
  .person-name {
    position: absolute; left: 28px; top: 1px;
    color: var(--card-white); font-size: 21px; font-weight: 400; line-height: 26px;
  }
  .brand-dot { position: absolute; left: 356px; top: 28px; }
  .personal-details, .company-details {
    position: absolute; left: 25px; list-style: none;
    font-size: 14.5px; line-height: 20px;
  }
  .personal-details { top: 65px; color: var(--ink-navy); }
  .company-details { top: 130px; color: var(--ink-teal); }
</style>
</head>
<body>
<main class="canvas">
  <section class="card card-front" aria-label="Card front">
    <p class="brand-name">Brindle Peak</p>
  </section>

  <section class="card card-back" aria-label="Card back">
    <div class="name-band">
      <h1 class="person-name">Owen Pritch</h1>
    </div>
    <svg class="brand-dot" width="70" height="100" viewBox="0 0 70 100" aria-hidden="true">
      <circle cx="35" cy="62" r="30" fill="var(--teal-mid)"/>
    </svg>
    <ul class="personal-details">
      <li>General Manager</li>
      <li>Mobile: +61 427 38 91 04</li>
      <li>Email: owen@brindlepeak.com.au</li>
    </ul>
    <ul class="company-details">
      <li>Tel: + 61 7 55 419 276</li>
      <li>www.brindlepeak.com.au</li>
      <li>Address: 3/47 Cordwell Parade</li>
      <li>Marlow Flats NSW 2593 Australia</li>
      <li>COMMERCIAL WATER FILTRATION EQUIPMENT</li>
    </ul>
  </section>
</main>
</body>
</html>
```